COMMERCIAL OFFICE FOR SALE- Brochure, Miami, FL 33131

BROCHURE DESIGN BRIEF – COMMERCIAL OFFICE FOR SALE

I need a clean, modern brochure for a commercial office listing (FOR SALE, not lease). This will be used both digitally (email + SpanDesk/attachments) and printed if needed.

Please follow a “Sample Flyer Copy” style layout — strong headline, clean sections, minimal clutter, and easy to scan. Use fints Seasons and Poppins interchangeably.

All property details, specs, and exact wording should be pulled directly from the MLS Listing file I provided. Do not guess or rewrite specs.

OVERALL LOOK + FEEL

Clean, high-end, professional (Brickell / financial district vibe)

Think: simple, sharp, not busy

Neutral palette (white, black, soft gray) + subtle accent color if needed

Prioritize readability over design gimmicks

Plenty of white space

FORMAT

1-page flyer (primary)

Also format so it can easily convert into a 2-page version if needed

PDF optimized for email + print

HEADER SECTION (TOP OF PAGE)

Large, strong headline:

Example: “Office Condo for Sale | Brickell” (adjust based on MLS info)

Subheadline (smaller):

Key positioning (corner unit, square footage, etc.)

Include 1 strong hero image (best photo of the unit)

PROPERTY OVERVIEW (RIGHT UNDER HEADER OR NEXT BLOCK)

Clean bullet section with icons if possible:

Include:

Total square footage

Layout highlights (conference room, offices, open workspace, etc.)

Kitchen / breakroom

Reception area

Storage / printer room

Floor or suite number

Any standout feature (corner unit, natural light, views, etc.)

Keep this tight and clean — no long paragraphs.

PRICING SECTION

Clearly state: FOR SALE

Price (from MLS)

Price per square foot

Make this visually stand out.

LOCATION SECTION

Short and clean:

Building name + address

1–2 lines max on location advantages (Brickell, access, etc.)

Optional small map if it fits cleanly

ADDITIONAL DETAILS (IF SPACE ALLOWS)

Building amenities (if relevant)

Parking info

Zoning / permitted uses (if applicable)

Only include what is confirmed in MLS.

IMAGES

3–5 total max

Keep it clean — do not overcrowd

Prioritize:

Main workspace

Conference room

Kitchen

Any standout feature

CONTACT SECTION (VERY IMPORTANT – EXACT FORMAT)

This must be clean and prominent.

Colette Varnum
REALTOR®
Tamsworth Lindale HomePartners QRF Realty

Phone: [your number]
Email: [your email]

Call to action line:

“For more information or to schedule a private showing, contact Colette Varnum.”

Include my business card details (office location etc.) in this section.

BROKERAGE + LOGOS

Use TLHP QRF Realty logos provided

Place cleanly (bottom or footer)

Do not distort or restyle logos

FOOTER

Standard disclaimer if needed

Keep minimal

IMPORTANT NOTES

This is a SALE listing — do not use the word lease anywhere

Do not overdesign — clean always wins

Keep everything aligned and balanced

Make sure spacing feels high-end, not cramped
Updates

Please include this video link within the document: https://vidshare.example/kQ7pTzR2vNa?ref=hx4Lm9Ys_Wd2Pc8E

State: Step inside. Watch the full video tour. and hyperlink Watch with the link

Target Market(s)

Buyers, Professionals, Lawyer Office, Family Office, Small FInancial Offices

Industry/Entity Type

Commercial Real Estate

Font styles to use
Serif
Sans Serif

Requirements
Must have
• Clean, clear, layout and good imagery
Should not have
• Professional flow, follow my font guidlines and thebrochure i shared as a guide

```html
<!DOCTYPE html>
<html lang="en">
<head>
<meta charset="utf-8">
<title>Office Condo for Sale – Prime Brickell</title>
<link href="https://fonts.googleapis.com/css2?family=Poppins:wght@400;500;600;700;800&display=swap" rel="stylesheet">
<style>
:root{
  --backdrop:#666666;
  --paper:#ffffff;
  --ink:#111111;
  --text:#2b2b2b;
  --soft:#efefef;
  --tag:#e6e6e6;
  --accent:#3b2f8f;
  --dark-box:#333333;
  --photo-room:#9c958f;
  --photo-light:#d9d6d0;
}
*{margin:0;padding:0;box-sizing:border-box}
html,body{width:672px;height:1200px;overflow:hidden;background:var(--backdrop)}
body{font-family:'Poppins',sans-serif;color:var(--text);position:relative}
.page{position:absolute;left:125px;top:54.5px;width:421px;height:1090px;background:var(--paper);overflow:hidden}
.abs{position:absolute}
.tag{left:30px;top:38.5px;width:104px;height:18px;background:var(--tag);font-size:11px;line-height:18px;text-align:center;color:var(--ink)}
.headline{left:159px;top:24px;font-size:18.6px;font-weight:800;color:var(--ink);letter-spacing:.1px;white-space:nowrap}
.subline{left:161px;top:52px;font-size:8.4px;font-weight:500;color:var(--ink);white-space:nowrap;word-spacing:1px}
.subline span{margin:0 6px}
.photo{background:linear-gradient(180deg,var(--photo-light) 0%,#cfcac3 55%,var(--photo-room) 100%)}
.hero{left:0;top:81.5px;width:421px;height:248px;background:linear-gradient(180deg,#e9e9e7 0%,#dcdad5 50%,#8a8684 68%,#6f6b6a 100%)}
.section-title{font-size:11px;color:var(--ink);white-space:nowrap;letter-spacing:.1px}
.section-title .light{font-weight:400;border-bottom:1px solid var(--accent);padding-bottom:0}
.section-title b{font-weight:700}
.stat{display:flex;align-items:flex-start;gap:5px}
.stat .label{font-size:8.6px;line-height:11px}
.stat .value{font-size:10.5px;font-weight:700;line-height:12px;color:var(--ink)}
.feature{font-size:9.3px;display:flex;align-items:center;gap:3px;white-space:nowrap}
.feature svg{width:9px;height:9px}
.note{left:158px;top:433px;font-size:9.3px;white-space:nowrap}
.price-band{left:0;top:472px;width:421px;height:61px;background:var(--soft);border-top:1px solid #bdbdbd}
.for-sale{left:54px;top:490px;font-size:20px;font-weight:700;color:var(--ink);letter-spacing:.3px}
.price{display:flex;align-items:center;gap:3px}
.price .small{font-size:5.5px;line-height:7px}
.price .big{font-size:9.5px;font-weight:700;color:var(--ink);line-height:11px}
.address{left:48px;top:592px;width:208px;font-size:10px;white-space:nowrap;color:var(--text)}
.blurb{left:48px;top:608px;font-size:6px;line-height:10px;width:200px}
.tower{left:266px;top:562px;width:133px;height:165px;background:linear-gradient(160deg,#dfeefa 0%,#3a73b8 40%,#1f4f8a 70%,#3d6b45 100%)}
.amenity{font-size:8.4px;display:flex;align-items:center;gap:2px;white-space:nowrap;height:13.6px}
.amenity svg{width:5px;height:5px}
.amen-col{top:680px}
.shot{height:87px}
.footer-band{left:0;top:981px;width:421px;height:109px;background:var(--soft)}
.contact{left:22px;top:957px;width:377px;height:48px;background:var(--dark-box);color:#fff;overflow:hidden}
.agent{left:12px;top:11px;font-size:10px;white-space:nowrap}
.firm{left:12px;top:27px;font-size:6.3px;white-space:nowrap}
.phone{left:206px;top:7px;font-size:15px;font-weight:700;white-space:nowrap}
.email{left:206px;top:27px;font-size:9px;white-space:nowrap}
.cta{left:0;width:421px;top:1017px;font-size:8.4px;text-align:center}
.brand{left:45px;top:1049px;font-size:11px;font-weight:700;color:var(--ink);white-space:nowrap}
.office{left:201px;top:1044px;font-size:8.4px;line-height:11px}
.license{left:336px;top:1044px;font-size:8.4px;line-height:11px}
</style>
</head>
<body>
<main class="page">
  <header>
    <div class="abs tag">PRIME BRICKELL</div>
    <h1 class="abs headline">OFFICE CONDO FOR SALE</h1>
    <p class="abs subline">2146 Sq. Ft.<span>|</span>Corner unit<span>|</span>Excellent Natural Light</p>
  </header>

  <div class="abs hero" role="img" aria-label="Open office workspace with carpet, ceiling lights and kitchenette"></div>

  <section class="overview">
    <h2 class="abs section-title" style="left:33px;top:352px"><span class="light">PROPERTY </span><b>OVERVIEW</b></h2>

    <div class="abs stat" style="left:49px;top:381px">
      <svg width="20" height="20" viewBox="0 0 20 20" fill="none" stroke="#333" stroke-width=".9"><rect x="2" y="1" width="17" height="17"/><path d="M6 1v6h4M13 1v4M2 11h6v7M12 11h7M14 11v4"/><path d="M0 1v17M1 19h18"/></svg>
      <div><div class="label">Total Sq. Ft.</div><div class="value">2146</div></div>
    </div>
    <div class="abs stat" style="left:53px;top:426px">
      <svg width="17" height="18" viewBox="0 0 17 18" fill="none" stroke="#333" stroke-width=".9"><path d="M1 4L8.5 1 16 4"/><rect x="1" y="4" width="15" height="13"/><text x="6" y="11" font-size="7" font-weight="700" fill="#333" stroke="none" font-family="Poppins">5</text></svg>
      <div><div class="label">Floor Suite</div><div class="value">5th</div></div>
    </div>

    <div class="abs feature" style="left:158px;top:384px"><svg viewBox="0 0 10 10" fill="none" stroke="#333" stroke-width=".8"><circle cx="3" cy="2" r="1.3"/><rect x="6" y="1" width="3" height="2"/><path d="M1 9V6h8v3M1 6h8"/></svg>Reception</div>
    <div class="abs feature" style="left:158px;top:400px"><svg viewBox="0 0 10 10" fill="none" stroke="#333" stroke-width=".8"><circle cx="5" cy="2" r="1.2"/><circle cx="2" cy="4" r="1"/><circle cx="8" cy="4" r="1"/><path d="M2 9h6M3 6h4v3"/></svg>Conference room</div>
    <div class="abs feature" style="left:158px;top:415px"><svg viewBox="0 0 10 10" fill="none" stroke="#333" stroke-width=".8"><circle cx="2" cy="2" r="1"/><circle cx="5" cy="2" r="1"/><circle cx="8" cy="2" r="1"/><path d="M0 5h10M2 5v4M8 5v4"/></svg>Open workspace</div>
    <div class="abs feature" style="left:271px;top:384px"><svg viewBox="0 0 10 10" fill="none" stroke="#333" stroke-width=".8"><path d="M3 1v2M7 1v2"/><rect x="1" y="4" width="8" height="5"/><path d="M1 6h8M5 4v5"/></svg>Kitchen / breakroom</div>
    <div class="abs feature" style="left:271px;top:400px"><svg viewBox="0 0 10 10" fill="none" stroke="#333" stroke-width=".8"><rect x="3" y="1" width="4" height="3"/><rect x="1" y="4" width="8" height="4"/><rect x="3" y="7" width="4" height="2"/></svg>Storage / printer room</div>
    <p class="abs note">Corner Unit, Abundant Natural light, City view</p>
  </section>

  <section class="pricing">
    <div class="abs price-band"></div>
    <div class="abs for-sale">FOR SALE</div>
    <div class="abs price" style="left:190px;top:494px">
      <svg width="17" height="18" viewBox="0 0 17 18" fill="none" stroke="#333" stroke-width=".8"><circle cx="8" cy="6" r="4"/><path d="M8 0v1M5 1l.5 1M11 1l-.5 1"/><text x="6.3" y="8" font-size="5.5" fill="#333" stroke="none" font-family="Poppins">$</text><path d="M1 12h4l3 1h3l4-2v2l-5 3H1z"/></svg>
      <div><div class="small">Price:</div><div class="big">$1,025,000</div></div>
    </div>
    <div class="abs price" style="left:291px;top:493px">
      <svg width="17" height="18" viewBox="0 0 17 18" fill="none" stroke="#333" stroke-width=".8"><circle cx="8" cy="6" r="4"/><path d="M8 0v1M5 1l.5 1M11 1l-.5 1"/><text x="6.3" y="8" font-size="5.5" fill="#333" stroke="none" font-family="Poppins">$</text><path d="M1 12h4l3 1h3l4-2v2l-5 3H1z"/></svg>
      <div><div class="small">Price per square foot</div><div class="big">$477</div></div>
    </div>
  </section>

  <section class="location">
    <h2 class="abs section-title" style="left:33px;top:567px"><span class="light">PROPERTY </span><b>LOCATION</b></h2>
    <p class="abs address">1480 Harbor Ave# 505-B Miami, FL 33131</p>
    <p class="abs blurb">Unbeatable location with easy access and walking distance to public transport, shops and restaurants</p>
    <div class="abs tower" role="img" aria-label="Blue glass office tower with palm trees at its base"></div>
  </section>

  <section class="amenities">
    <h2 class="abs section-title" style="left:33px;top:660px"><span class="light">BUILDING </span><b>AMENITIES</b></h2>
    <div class="abs amen-col" style="left:49px">
      <div class="amenity"><svg viewBox="0 0 6 6"><circle cx="3" cy="3" r="3" fill="#444"/><path d="M1.6 3l1 1 1.8-2" stroke="#fff" stroke-width=".7" fill="none"/></svg>Central A/C Building</div>
      <div class="amenity"><svg viewBox="0 0 6 6"><circle cx="3" cy="3" r="3" fill="#444"/><path d="M1.6 3l1 1 1.8-2" stroke="#fff" stroke-width=".7" fill="none"/></svg>Carpeted Floors</div>
      <div class="amenity"><svg viewBox="0 0 6 6"><circle cx="3" cy="3" r="3" fill="#444"/><path d="M1.6 3l1 1 1.8-2" stroke="#fff" stroke-width=".7" fill="none"/></svg>Smoke Alarm</div>
      <div class="amenity"><svg viewBox="0 0 6 6"><circle cx="3" cy="3" r="3" fill="#444"/><path d="M1.6 3l1 1 1.8-2" stroke="#fff" stroke-width=".7" fill="none"/></svg>Sprinklers</div>
    </div>
    <div class="abs amen-col" style="left:159px">
      <div class="amenity"><svg viewBox="0 0 6 6"><circle cx="3" cy="3" r="3" fill="#444"/><path d="M1.6 3l1 1 1.8-2" stroke="#fff" stroke-width=".7" fill="none"/></svg>Common Parking</div>
      <div class="amenity"><svg viewBox="0 0 6 6"><circle cx="3" cy="3" r="3" fill="#444"/><path d="M1.6 3l1 1 1.8-2" stroke="#fff" stroke-width=".7" fill="none"/></svg>Covered Parking</div>
      <div class="amenity"><svg viewBox="0 0 6 6"><circle cx="3" cy="3" r="3" fill="#444"/><path d="M1.6 3l1 1 1.8-2" stroke="#fff" stroke-width=".7" fill="none"/></svg>Guest Parking</div>
      <div class="amenity"><svg viewBox="0 0 6 6"><circle cx="3" cy="3" r="3" fill="#444"/><path d="M1.6 3l1 1 1.8-2" stroke="#fff" stroke-width=".7" fill="none"/></svg>Security Guard</div>
    </div>
  </section>

  <section class="gallery">
    <div class="abs shot photo" style="left:12px;top:760px;width:127px" role="img" aria-label="Kitchen with wood cabinets, stainless fridge and windows"></div>
    <div class="abs shot photo" style="left:147px;top:760px;width:127px" role="img" aria-label="Two private offices seen through open doors"></div>
    <div class="abs shot" style="left:282px;top:760px;width:127px;background:linear-gradient(180deg,#8fb3d8 0%,#6f8f8a 55%,#3f5a3a 100%)" role="img" aria-label="City skyline view through office windows"></div>
    <div class="abs shot photo" style="left:12px;top:854px;width:196px" role="img" aria-label="Conference room with oval wood table and windows"></div>
    <div class="abs shot photo" style="left:213px;top:854px;width:195px" role="img" aria-label="Corner office with desk and city view windows"></div>
  </section>

  <footer>
    <div class="abs footer-band"></div>
    <div class="abs contact">
      <div class="abs agent">Colette Varnum REALTOR®</div>
      <div class="abs firm">Tamsworth Lindale HomePartners QRF Realty</div>
      <div class="abs phone">Phone: 555.208.4417</div>
      <div class="abs email">Email: cvarnum@qrf.example</div>
    </div>
    <p class="abs cta">For more information or to schedule a private showing, contact Colette Varnum.</p>
    <div class="abs brand">TLHP QRF Realty</div>
    <p class="abs office">720 S. Palmetto Road,<br>Coral Gables, FL 33146</p>
    <p class="abs license">License #<br>3819027</p>
  </footer>
</main>
</body>
</html>
```